Bluestone Advisory & Mgmt - Professional Business Cards

Hi!

I am a Real Estate Developer and Construction Consultant.

I have a lot of inspiration from previous designs and would be open to using the attached Designs as a starting point. I would like to see these styles incorporated into your designs.

I really need professional business card to go with it that includes my important info.

Look forward to seeing your designs!.

Target Market(s)

My Target market are building owners, lawyers, consultants.

Industry/Entity Type

Real Estate Development

Contact Information for Business Card

My Name: Dorian Pelkey
My Title: Principle
Company Name: Bluestone Advisory & Mgmt, LLC
Address: 348 West 71st Street, 9th FL New York, NY 10010
Mobile: 917.806.3971
Website: bam-hvx.example

Font styles to use
Serif
Sans Serif

Colors

Designer to choose colors to be used in the design.

Requirements
Must have
• Must incorporate the logo attached or have new that looks similar.
• Must use professional font that will be seen and judged by wealthy land owners and developers.
• Must incorporate some of the color green.
Should not have
• Photo's or pictures of people or buildings of any kind.

```html
<!DOCTYPE html>
<html lang="en">
<head>
<meta charset="utf-8">
<title>Bluestone Advisory &amp; Mgmt - Business Cards</title>
<link rel="stylesheet" href="https://fonts.googleapis.com/css2?family=Arimo:wght@400;700&family=Montserrat:wght@400&family=Open+Sans:wght@400&display=swap">
<style>
  :root {
    --bg-top: #2e2e2e;
    --bg-bottom: #0c0c0c;
    --card: #1f1f1f;
    --card-edge: #2a2a2a;
    --green: #3fbf78;
    --grey: #8a8a8a;
    --grey-light: #b4b4b4;
  }
  * { margin: 0; padding: 0; box-sizing: border-box; }
  html, body {
    width: 1200px; height: 900px; overflow: hidden;
  }
  body {
    background: radial-gradient(ellipse at 70% 20%, var(--bg-top), var(--bg-bottom) 75%);
    position: relative;
    font-family: "Arimo", Arial, sans-serif;
  }
  .card {
    position: absolute;
    left: 285px;
    width: 630px;
    height: 360px;
    background: var(--card);
    border: 1px solid var(--card-edge);
    box-shadow: 0 18px 40px rgba(0,0,0,0.6);
  }
  .card--front { top: 65px; }
  .card--back { top: 475px; }

  .front-name {
    position: absolute;
    left: 0; right: 0; top: 130px;
    text-align: center;
    font-family: "Montserrat", Arial, sans-serif;
    font-weight: 400;
    font-size: 34px;
    line-height: 1.25;
    color: var(--grey);
  }

  .company {
    position: absolute;
    left: 46px; top: 142px;
    font-family: "Open Sans", Arial, sans-serif;
    font-weight: 400;
    font-size: 25px;
    line-height: 1.2;
    color: var(--green);
  }
  .divider {
    position: absolute;
    left: 322px; top: 78px;
    width: 2px; height: 204px;
    background: var(--green);
  }
  .contact {
    position: absolute;
    left: 352px; top: 86px;
    width: 260px;
  }
  .contact__name {
    font-weight: 700;
    font-size: 22px;
    color: var(--green);
    letter-spacing: 0.5px;
  }
  .contact__title {
    font-size: 15px;
    color: var(--grey);
    margin-top: 1px;
  }
  .contact__address {
    font-size: 14px;
    line-height: 1.3;
    color: var(--green);
    margin-top: 22px;
  }
  .contact__list {
    list-style: none;
    margin-top: 22px;
  }
  .contact__item {
    display: flex;
    align-items: center;
    gap: 12px;
    font-size: 14px;
    color: var(--grey-light);
    height: 22px;
  }
  .contact__icon {
    width: 16px; height: 16px;
    flex: none;
  }
</style>
</head>
<body>
  <section class="card card--front" aria-label="Card front">
    <p class="front-name">Bluestone Advisory<br>&amp; Management</p>
  </section>

  <section class="card card--back" aria-label="Card back">
    <p class="company">Bluestone Advisory<br>&amp; Mgmt, LLC</p>
    <div class="divider"></div>
    <div class="contact">
      <p class="contact__name">Dorian Pelkey</p>
      <p class="contact__title">Principle</p>
      <p class="contact__address">348 West 71st Street, 9th FL<br>New York, NY 10010</p>
      <ul class="contact__list">
        <li class="contact__item">
          <svg class="contact__icon" viewBox="0 0 16 16" aria-hidden="true"><path d="M3.5 1.5l2.5 3-1.5 1.5c.8 2 2.5 3.7 4.5 4.5l1.5-1.5 3 2.5-1.5 2.5C7 14 2 9 1 3z" fill="var(--green)"/></svg>
          917.806.3971
        </li>
        <li class="contact__item">
          <svg class="contact__icon" viewBox="0 0 16 16" aria-hidden="true"><rect x="1" y="3.5" width="14" height="9" fill="none" stroke="var(--green)" stroke-width="1.3"/><path d="M1 3.5l7 5.5 7-5.5" fill="none" stroke="var(--green)" stroke-width="1.3"/></svg>
          dorian@bam-hvx.example
        </li>
        <li class="contact__item">
          <svg class="contact__icon" viewBox="0 0 16 16" aria-hidden="true"><g fill="none" stroke="var(--green)" stroke-width="1.2"><circle cx="8" cy="8" r="6.5"/><ellipse cx="8" cy="8" rx="3" ry="6.5"/><path d="M1.5 8h13M2.5 4.8h11M2.5 11.2h11"/></g></svg>
          www.bam-hvx.example
        </li>
      </ul>
    </div>
  </section>
</body>
</html>
```